Come crowdsource a Web Design for a brazilian crowdsource Startup!

> NAME OF OUR STARTUP:
Mundaleo

> DESCRIPTION OF OUR STARTUP:
We are a crowdsourcing startup in Brazil providing consultancy and technology to support other companies to crowdsource their projects.
We also operate doing big crowdsource campaings related to polemic subjects in Brazil.

> WHAT ARE OUR TARGET AUDIENCE?
Our target audience are young people around 20-35 years old.
Generation Y (Millennial Generation)

> WHAT IS OUR INDUSTRY?
Internet, web

> WHAT DO WE NEED?
We need a Web Design for our first site.

We need 5 pages:
- Home
- What is Crowdsourcing?
- Solutions
- About Us
- Blog
- A box for the "Contact" tab (this is not a page)

Please, find attached a Layout Sketch of what I've imagined.

Lets talk about the sketch:
Well, first of all, it's a SKETCH, so you don't have to send proposals exactly as the sketch. The sketch is just to show how I've imagined the ditribution of the content boxes. For example, the menu bar doesnt need to be a rectangle exactly like the sketch, but, I would like to have the menu on the right side of the logo. Also, you will see that the boxes are all squeezed, of course I dont want them soo squeezed! Again, its juust a SKETCH!

About the images on the sketch:
IMG1 - Some nice and simple image related to collectivity or related to crowdsourcing or maybe use our O logo.

IMG2 - Some simple and creative image related to Consultancy. It doesnt need to be so obvious.

IMG3 - Some simple and creative image related to Web 2.0 Software Technology. It doesnt need to be so obvious.

IMG4 - Some simple and creative image related to a full package of Consultancy + Technology. It doesnt need to be so obvious.

IMG5 - Some nice and simple image related to collectivity or related to crowdsourcing.

IMG6 - Some nice and simple image related to Ideation. Maybe a light bulb? I dont know, be creative!

IMG7 - Some nice and simple image related to Crowdlabor. I dont know, be creative!

IMG8 - Some nice and simple image related to CrowdFeedback. Maybe a megaphone? A loudspeaker? I dont know, be creative!

IMG9 - Some nice and simple image related to us! Maybe our O logo ? I dont know, be creative!

THE CONTACT SIDE BAR - we need a nice and simple contact side bar. By the way, on the sketch this bar is shown only at the homepage, but when the site becomes real this bar will stay along all the pages.

THE CONTACT BOX - we need a nice and simple contact box.

ABOUT THE COLORS TO USE: we would like some color to our background and titles. We like colors similars to our logo: really light blue ? light green/blue ? light grey ? light orange ? I dont know, you guys knows more about that then me =)

CHATTERBOX SHARE/LIKE BUTTON: We would like a chatterbox share/like button somewhere on the site!

ABOUT THE ATTACHED FILES:

ADDITIONALS:
> The name Mundaleo comes from "collectivity". With our name we want to pass the idea of the collectivity from the crowdsource work model.

> Our communication is directed to the Generation Y.

> Remember, we are a Startup! So we need a modern and simple site, something like the web 2.0 trends. It must be beautiful =)

> We arent a serious company. We are a young and fun company! Please, dont come with old fashionable company sites.

> Be creative =] !

Target Market(s)

Our target audience are young people around 20-35 years old. Generation Y (Millennial Generation)

Industry/Entity Type

Communication

Requirements
Must have
• We need a Web Design for our first site.

We need 5 pages:
- Home
- What is Crowdsourcing?
- Solutions
- About Us
- Blog

ABOUT THE COLORS TO USE: we would like some color to our background and titles. We like colors similars to our logo: really light blue ? light green/blue ? light grey ? light oranges ? I dont know, you guys knows more about that then me =)

Should not have
• Poor/serious/old fashionable designs

```html
<!DOCTYPE html>
<html lang="en">
<head>
<meta charset="utf-8">
<title>Mundaleo – Projects</title>
<link href="https://fonts.googleapis.com/css2?family=Hind:wght@400;500&display=swap" rel="stylesheet">
<style>
:root{
  --cyan:#06d9ef;
  --white:#ffffff;
  --sun:#fbbb22;
  --label:#fbb92a;
  --track:#d4d4d4;
  --teal:#14a89c;
  --orange:#ff8a10;
  --magenta:#b0127a;
  --lime:#8ee212;
  --blue:#13a3f2;
  --dot:#c8c8c8;
  --dot-active:#17a7b8;
}
*{margin:0;padding:0;box-sizing:border-box}
html,body{width:1200px;height:1000px;overflow:hidden}
body{background:var(--cyan);font-family:"Hind",Arial,sans-serif;position:relative;color:var(--white)}
.page-panel{position:absolute;left:100px;top:0;width:1000px;height:590px;background:var(--white)}
.showcase-band{position:absolute;left:100px;top:300px;width:1000px;height:163px;background:var(--cyan)}
.project-card{position:absolute;top:0;width:182px;height:201px}
.project-photo{position:absolute;left:3px;top:0;width:177px;height:131px;border-radius:14px 14px 0 0}
.project-label{position:absolute;left:0;top:131px;width:182px;height:63px;background:var(--label);border:1px solid #f0a818}
.project-title{position:absolute;left:0;top:141px;width:182px;text-align:center;font-size:18px;font-weight:500;letter-spacing:-0.2px}
.progress-track{position:absolute;left:6px;top:176px;width:168px;height:24px;border-radius:12px;background:var(--track);border:2px solid #c2c2c2;overflow:hidden}
.progress-fill{height:100%;border-radius:12px;background-image:repeating-linear-gradient(135deg,rgba(255,255,255,.12) 0 4px,transparent 4px 8px)}
.slider{position:absolute;left:119px;top:243px;width:608px;height:292px;box-shadow:0 10px 14px rgba(0,0,0,.15)}
.slide-photo{width:100%;height:100%;background:linear-gradient(100deg,#6b5a3e 0%,#3a3a2e 45%,#2e2f2a 70%,#7a7a78 100%)}
.slider-arrow{position:absolute;top:125px;width:45px;height:45px;background:linear-gradient(#ffd23a,#f5a60f);border-radius:3px}
.slider-arrow svg{display:block}
.slider-dots{position:absolute;left:370px;top:560px;display:flex;gap:7px}
.slider-dots span{width:14px;height:14px;border-radius:50%;background:var(--dot);border:1px solid #a8a8a8}
.slider-dots .is-active{background:var(--dot-active)}
.showcase-heading{position:absolute;left:752px;top:302px;width:340px;font-size:38px;font-weight:500;line-height:54px}
.site-footer{position:absolute;left:0;top:590px;width:1200px;height:410px;background:var(--sun)}
.footer-heading{position:absolute;top:36px;font-size:46px;font-weight:500;text-align:center;width:300px}
.footer-links{position:absolute;left:130px;top:106px;font-size:20px;line-height:37px}
.footer-links a{position:absolute;color:var(--white);text-decoration:none;white-space:nowrap}
.subscribe-box{position:absolute;left:487px;top:115px;width:231px;height:54px;background:#fdfdfd;border:1px solid #e0a520;border-radius:3px}
.email-field{position:absolute;left:12px;top:10px;width:205px;height:33px;border:1px solid #ccc;border-radius:4px;padding-left:9px;font:15px Arial,sans-serif;color:#c4c4c4;line-height:31px}
.privacy-note{position:absolute;left:470px;top:177px;width:104px;text-align:right;font-size:16px;line-height:21px}
.subscribe-button{position:absolute;left:581px;top:176px;width:137px;height:44px;background:var(--cyan);border-radius:3px;text-align:center;font-size:18px;line-height:46px;box-shadow:0 4px 4px rgba(0,0,0,.2)}
.contact-details{position:absolute;left:793px;top:105px;font-size:20px;line-height:37px}
.contact-details small{font-size:16px}
.footer-brand{position:absolute;left:0;top:288px;width:1200px;text-align:center;font-size:24px;font-weight:500;display:flex;justify-content:center;align-items:center;gap:8px}
.footer-brand i{width:18px;height:18px;border-radius:50%;background:var(--white)}
.copyright{position:absolute;left:0;top:346px;width:1200px;text-align:center;font-size:35px;font-weight:500;white-space:nowrap}
</style>
</head>
<body>
<div class="page-panel"></div>
<div class="showcase-band"></div>

<section class="projects">
  <div class="project-card" style="left:124px">
    <div class="project-photo" role="img" aria-label="Sketch of plan, collaborate and deliver steps with coloured blocks" style="background:linear-gradient(#eef0f0,#d8dcdc)"></div>
    <div class="project-label"></div><div class="project-title">Awesome Project 1</div>
    <div class="progress-track"><div class="progress-fill" style="width:117px;background-color:var(--teal)"></div></div>
  </div>
  <div class="project-card" style="left:316px">
    <div class="project-photo" role="img" aria-label="Project manager app on a tablet and phone" style="background:linear-gradient(120deg,#e6e6e6,#3b3b3b)"></div>
    <div class="project-label"></div><div class="project-title">Awesome Project 2</div>
    <div class="progress-track"><div class="progress-fill" style="width:117px;background-color:var(--orange)"></div></div>
  </div>
  <div class="project-card" style="left:509px">
    <div class="project-photo" role="img" aria-label="Portrait photo of a young girl" style="background:linear-gradient(#5a4436,#a47a60)"></div>
    <div class="project-label"></div><div class="project-title">Awesome Project 3</div>
    <div class="progress-track"><div class="progress-fill" style="width:107px;background-color:var(--magenta)"></div></div>
  </div>
  <div class="project-card" style="left:701px">
    <div class="project-photo" role="img" aria-label="Colourful collage of media and hobby objects" style="background:linear-gradient(135deg,#2a8fd0,#f08a20 55%,#3a6fc0)"></div>
    <div class="project-label"></div><div class="project-title">Awesome Project 4</div>
    <div class="progress-track"><div class="progress-fill" style="width:137px;background-color:var(--lime)"></div></div>
  </div>
  <div class="project-card" style="left:894px">
    <div class="project-photo" role="img" aria-label="Coloured jigsaw puzzle pieces" style="background:linear-gradient(135deg,#e8e8e8 40%,#f2b418 60%,#3aa0d8)"></div>
    <div class="project-label"></div><div class="project-title">Awesome Project 5</div>
    <div class="progress-track"><div class="progress-fill" style="width:87px;background-color:var(--blue)"></div></div>
  </div>
</section>

<section class="slider">
  <div class="slide-photo" role="img" aria-label="Young woman working at a laptop"></div>
  <div class="slider-arrow" style="left:11px">
    <svg width="45" height="45" viewBox="0 0 45 45"><path d="M26 13 L17 22.5 L26 32" fill="none" stroke="#fff" stroke-width="4"/></svg>
  </div>
  <div class="slider-arrow" style="left:554px">
    <svg width="45" height="45" viewBox="0 0 45 45"><path d="M19 13 L28 22.5 L19 32" fill="none" stroke="#fff" stroke-width="4"/></svg>
  </div>
</section>
<div class="slider-dots"><span></span><span></span><span></span><span class="is-active"></span><span></span><span></span></div>

<h2 class="showcase-heading">Here are some projects Mundaleo has helped realise!</h2>

<footer class="site-footer">
  <h3 class="footer-heading" style="left:83px">Links</h3>
  <h3 class="footer-heading" style="left:453px">Subscribe</h3>
  <h3 class="footer-heading" style="left:780px">Contact Us</h3>

  <nav class="footer-links">
    <a href="#" style="left:0;top:0">Home</a>
    <a href="#" style="left:85px;top:0">About</a>
    <a href="#" style="left:185px;top:0">Crowdfund</a>
    <a href="#" style="left:0;top:37px">Blog</a>
    <a href="#" style="left:85px;top:37px">Projects</a>
    <a href="#" style="left:202px;top:37px">Contact</a>
  </nav>

  <div class="subscribe-box"><div class="email-field">Email Address</div></div>
  <div class="privacy-note">View Our Privacy Policy</div>
  <div class="subscribe-button">Subscribe</div>

  <div class="contact-details">
    <div>Office Hours: 10 A.M. to 6 P.M.</div>
    <div>Tel: +55 11 4020 7788</div>
    <div>E-mail: <small>info@mundaleo.com</small></div>
  </div>

  <div class="footer-brand"><i></i>Mundaleo</div>
  <p class="copyright">Copyright 2013&nbsp; Mundaleo. All rights reserved.</p>
</footer>
</body>
</html>
```